Radiant Harbor Holdings business card

We are a real estate advisory and investment company. We are specialized in assisting high networth individuals to invest in real estate overseas. We deliver a very personalized service, anticipating all the potential challenges an investor can face, and making it easy and safe for them. We also co-invest with our clients, assuring them that each project will be looked after as it is our own, and at the same time giving them the extra booth on confidence to invest.

We need a business card design. The business card must have a very premium, high-end look, reflecting principles like "commitment", "trust" and "timeless (but contemporary)". We look for long term relationships with our clients, and we grow with their referrals. We are all about conquering the confidence of the clients by always delivering above the expectations performance.

Target Market(s)

High net worth individuals.

Industry/Entity Type

Real Estate

Contact Information for Business Card

Please consider places on the business card for:

Name
Function (bellow name in smaller size text)

Mobile phone
E-mail
Skype ID
WeChat ID

Adress (3 lines)

Also include the following locations references:
NORVALE * ASHMERE * KELDPORT

Website: www.rhholdings.example

Requirements
Must have
• Company Logo

```html
<!DOCTYPE html>
<html lang="en">
<head>
<meta charset="UTF-8">
<title>Radiant Harbor Holdings — Business Card</title>
<link href="https://fonts.googleapis.com/css2?family=Cinzel:wght@500&family=Playfair+Display:wght@700&family=Open+Sans:wght@400;700&display=swap" rel="stylesheet">
<style>
  :root {
    --page-bg: #eeebec;
    --card-bg: #050607;
    --brand-blue: #2aa6e0;
    --text-white: #ffffff;
  }
  * { box-sizing: border-box; margin: 0; padding: 0; }
  html, body {
    width: 1200px; height: 1200px; overflow: hidden;
    background: var(--page-bg);
  }
  .sheet {
    width: 1200px; height: 1200px;
    display: flex; flex-direction: column;
    align-items: center; justify-content: center; gap: 64px;
  }
  .card {
    width: 840px; height: 480px;
    background: var(--card-bg);
    border-radius: 44px;
    box-shadow: 0 18px 40px rgba(0,0,0,0.35);
    position: relative;
    color: var(--text-white);
  }
  .card--front {
    display: flex; align-items: center; justify-content: center;
  }
  .brand {
    display: flex; align-items: center; gap: 22px;
  }
  .brand__dot {
    width: 26px; height: 26px; border-radius: 50%;
    background: var(--brand-blue);
    flex: none;
  }
  .brand__name {
    font-family: "Cinzel", serif;
    font-weight: 500;
    font-size: 44px;
    letter-spacing: 2px;
    color: var(--brand-blue);
    white-space: nowrap;
  }
  .card--back {
    display: flex; flex-direction: column; align-items: center;
    padding-top: 96px;
    font-family: "Open Sans", sans-serif;
  }
  .person {
    display: flex; align-items: center; gap: 14px;
  }
  .person__name {
    font-family: "Playfair Display", serif;
    font-weight: 700;
    font-size: 50px;
    line-height: 1;
    letter-spacing: 1px;
  }
  .person__divider {
    width: 2px; height: 34px; background: var(--text-white);
  }
  .person__role {
    font-size: 17px;
    align-self: flex-start;
    margin-top: -4px;
  }
  .details {
    margin-top: 70px;
    text-align: center;
    font-size: 22px;
    line-height: 1.45;
  }
  .details__label { font-weight: 700; }
  .contact-line {
    position: absolute; left: 0; right: 0; bottom: 52px;
    text-align: center;
    font-size: 22px;
    white-space: nowrap;
  }
</style>
</head>
<body>
  <main class="sheet">
    <section class="card card--front" aria-label="Card front">
      <div class="brand">
        <span class="brand__dot"></span>
        <span class="brand__name">Radiant Harbor Holdings</span>
      </div>
    </section>

    <section class="card card--back" aria-label="Card back">
      <div class="person">
        <span class="person__name">JOHN DOE</span>
        <span class="person__divider"></span>
        <span class="person__role">Director</span>
      </div>
      <div class="details">
        <p>Dummy city, Dummy Country, Land Dummy</p>
        <p>NORVALE * ASHMERE * KELDPORT</p>
        <p><span class="details__label">M.</span> 1-234-567890</p>
      </div>
      <p class="contact-line"><span class="details__label">W.</span> www.rhholdings.example | Skype &amp; WeChat ID. rhholdings</p>
    </section>
  </main>
</body>
</html>
```